Create the design of Sitepelican (in photoshop or similar)

*edit* What we wanna see is a sketch of a first page, and then in the end 5 page designs, but the main page will be the big tasks other pages are just basically pop-ups or form. *edit*

We need a web design for our new startup Sitepelican in turn will be providing web pages to smaller business. So the purpose of the page is to clearly showcase the message in a web 3.0 fashion, good design looks but function should always be the main focus.Further more we are looking for a long term relationship with a good designer / design company that can help us design the future web sites for our customers as well.

We need you to understand web, not just design. You need to be up to date with how web looks and works, and how to make it as simple and easy to use as possible for the customer and at the same time good looking.

Please look at the PDF for full description of the project.

Colors and layout are free to choose, but we really like the kind of layout that forkglider.com has so feel free to be inspired by them.

We want all of the pages design, but the main/landing page will be the big part, the rest are small pages that will use the same design frame as the main page.

PS. We just want the design in photoshop or illustrator format, the website will then be built in page tidal by page tidal experts (let us know if you/company also possess this knowledge)

Target Market(s)

Small to medium sized business, mostly owner/entrepreneur driven companies.

Industry/Entity Type

Business

Font styles to use
Other font styles liked:
• Helvetica for the win

Requirements
Must have
• Great and simple design, a child should be able to understand the message and also enjoy reading it. Should be a funny website while still being professional, i.e. see postbadger.com for example.

```html
<!DOCTYPE html>
<html lang="en">
<head>
<meta charset="utf-8">
<title>Sitepelican – Most Convenient Web Ever</title>
<link rel="stylesheet" href="https://fonts.googleapis.com/css2?family=Bebas+Neue&family=Open+Sans:wght@400;600;700&family=Montserrat:wght@400;600&family=Raleway:wght@300;400&display=swap">
<style>
:root{
  --navy:#063a5a;
  --orange:#f58a2c;
  --orange-btn:#f7852a;
  --grey-bg:#f2f2f2;
  --text:#4a4a4a;
  --btn-dark:#2f4456;
  --sky:#6f9cc6;
  --mint:#e8f5f5;
  --demo:#4f86c6;
  --white:#ffffff;
}
*{margin:0;padding:0;box-sizing:border-box}
html,body{width:1200px;height:3051px;overflow:hidden}
body{position:relative;background:var(--white);font-family:"Open Sans",Arial,sans-serif;color:var(--text)}
.abs{position:absolute}
.heading{font-family:"Bebas Neue",Impact,sans-serif;color:var(--orange);font-weight:400;letter-spacing:1px;line-height:1.2}
.body-copy{font-size:14.5px;line-height:26px;color:var(--text)}
.btn-dark{display:flex;align-items:center;justify-content:center;background:var(--btn-dark);color:var(--white);font-family:"Montserrat",Arial,sans-serif;font-weight:600;font-size:13px;border-radius:4px;text-transform:uppercase}
.art{border-radius:8px}

/* header */
.site-header{left:0;top:0;width:1200px;height:134px;background:var(--white)}
.brand{display:flex;flex-direction:column;align-items:center}
.brand-mark{width:46px;height:46px;border-radius:50%;background:var(--navy)}
.brand-name{font-family:"Open Sans",Arial,sans-serif;font-weight:400;color:var(--navy);font-size:28px;line-height:1.1;margin-top:2px}
.brand-tag{font-size:11px;color:var(--navy)}
.nav-item{top:50px;height:32px;display:flex;align-items:center;font-family:"Montserrat",Arial,sans-serif;font-size:14px;color:#333}
.nav-home{left:515px;width:76px;justify-content:center;background:var(--navy);color:var(--white);border-radius:4px;font-weight:600}
.nav-order{left:1004px;top:47px;width:87px;height:38px;justify-content:center;background:var(--orange-btn);color:var(--white);border-radius:4px}

/* hero */
.hero{left:0;top:134px;width:1200px;height:574px;background:var(--navy)}
.hero-title{left:112px;top:140px;font-size:66px}
.hero-points{left:112px;top:222px;list-style:none}
.hero-points li{font-family:"Bebas Neue",Impact,sans-serif;color:var(--white);font-size:24px;line-height:32.5px;letter-spacing:.6px;display:flex;align-items:center}
.hero-points svg{margin-right:14px}
.hero-points li.cont{padding-left:36px}
.hero-btn{left:148px;top:342px;width:107px;height:35px;background:var(--white);color:var(--navy);display:flex;align-items:center;justify-content:center;font-family:"Montserrat",Arial,sans-serif;font-weight:600;font-size:13px;border-radius:4px}
.hero-art{left:520px;top:59px;width:530px;height:480px;background:radial-gradient(ellipse at 60% 40%,#e95b3a 0,#d9d9d9 12%,rgba(140,180,220,.5) 30%,rgba(6,58,90,0) 65%)}
.cloud-band{left:0;top:518px;width:1200px;height:56px;background:var(--sky)}
.scroll-cue{left:563px;top:543px;width:74px;height:37px;background:var(--white);border-radius:37px 37px 0 0;display:flex;justify-content:center;padding-top:10px}

/* feature rows */
.row{left:0;width:1200px}
.row-grey{background:var(--grey-bg)}
.row-white{background:var(--white)}

/* pricing band */
.price-band{left:0;top:1635px;width:1200px;height:118px;background:var(--navy)}
.price-band-text{left:112px;top:38px;font-family:"Bebas Neue",Impact,sans-serif;color:var(--white);font-size:36px;letter-spacing:1px}
.price-band-btn{left:803px;top:30px;width:289px;height:58px;background:var(--orange-btn);color:var(--white);font-family:"Montserrat",Arial,sans-serif;font-size:22px;display:flex;align-items:center;justify-content:center;border-radius:3px}

/* partner */
.partner{display:flex;align-items:center}
.partner-mark{width:40px;height:40px;background:var(--btn-dark);margin-right:12px}
.partner-name{font-family:"Open Sans",Arial,sans-serif;font-weight:400;font-size:30px;color:var(--btn-dark)}

/* calculator */
.calc{left:0;top:2010px;width:1200px;height:384px;background:var(--mint)}
.calc-title{left:0;top:52px;width:1200px;text-align:center;font-family:"Raleway",Arial,sans-serif;font-weight:400;color:#4d5a66;font-size:36px;line-height:47px}
.field{top:179px;height:53px;background:var(--white);border:1px solid #dde6e6;border-radius:27px;display:flex;align-items:center;padding-left:22px;font-size:12px;color:#555}
.calc-btn{left:494px;top:270px;width:212px;height:57px;border-radius:28px;background:linear-gradient(#e9392c,#b71c13);color:var(--white);font-family:"Montserrat",Arial,sans-serif;font-size:17px;display:flex;align-items:center;justify-content:center;box-shadow:0 4px 6px rgba(0,0,0,.25)}

/* pricing details */
.details-title{left:0;width:1200px;text-align:center;font-size:40px}
.demo-btn{left:454px;top:2697px;width:292px;height:50px;border-radius:25px;background:var(--demo);color:var(--white);font-family:"Montserrat",Arial,sans-serif;font-size:19px;letter-spacing:1px;display:flex;align-items:center;justify-content:center}

/* footer */
.site-footer{left:0;top:2807px;width:1200px;height:244px;background:var(--navy)}
.foot-head{font-family:"Montserrat",Arial,sans-serif;color:var(--white);font-size:17px;font-weight:400}
.foot-line{font-size:11px;color:var(--white);line-height:22px}
.foot-divider{top:20px;width:1px;height:160px;background:#335d78}
.social{top:76px;width:32px;height:32px;border-radius:50%;background:#0d2436}
.sub-input{left:474px;top:159px;width:177px;height:33px;background:#e6e6e6;font-size:11px;color:#555;display:flex;align-items:center;padding-left:10px}
.sub-go{left:651px;top:159px;width:35px;height:33px;background:#17202a;color:var(--white);font-size:13px;display:flex;align-items:center;justify-content:center}
.contact-tab{left:830px;top:210px;width:252px;height:34px;background:#5e6468;border:1px solid #999;color:var(--white);font-family:"Montserrat",Arial,sans-serif;font-size:15px;display:flex;align-items:center;justify-content:space-between;padding:0 18px}
</style>
</head>
<body>

<header class="site-header abs">
  <div class="brand abs" style="left:96px;top:14px;width:200px">
    <div class="brand-mark"></div>
    <div class="brand-name">Sitepelican</div>
    <div class="brand-tag">Most Convenient Web Ever</div>
  </div>
  <nav>
    <a class="nav-item nav-home abs">Home</a>
    <a class="nav-item abs" style="left:622px">How it works</a>
    <a class="nav-item abs" style="left:752px">About</a>
    <a class="nav-item abs" style="left:841px">Contact</a>
    <a class="nav-item abs" style="left:938px">Faq</a>
    <a class="nav-item nav-order abs">Order Now</a>
  </nav>
</header>

<section class="hero abs">
  <div class="hero-art abs art" role="img" aria-label="Illustration of a red and white rocket launching up from clouds into a starry sky"></div>
  <h1 class="heading hero-title abs">What is Sitepelican?</h1>
  <ul class="hero-points abs">
    <li><svg width="22" height="18" viewBox="0 0 22 18"><path d="M1 9 21 1 14 17 11 10z" fill="#fff"/></svg>Your website on subscription autopilot with free</li>
    <li class="cont">unlimited support and updates.</li>
    <li><svg width="22" height="18" viewBox="0 0 22 18"><path d="M1 9 21 1 14 17 11 10z" fill="#fff"/></svg>Delivered by professionals.</li>
  </ul>
  <a class="hero-btn abs">LEARN MORE</a>
  <div class="cloud-band abs"></div>
  <div class="scroll-cue abs"><svg width="18" height="12" viewBox="0 0 18 12"><path d="M2 2 9 9 16 2" fill="none" stroke="#f58a2c" stroke-width="2.5"/></svg></div>
</section>

<section class="row row-grey abs" style="top:708px;height:329px">
  <div class="abs art" style="left:158px;top:49px;width:184px;height:232px;background:radial-gradient(circle at 50% 60%,#e8dcc0,#c8a86b 60%,#f2f2f2 75%)" role="img" aria-label="Illustration of a money bag with a dollar sign and gold bars"></div>
  <h2 class="heading abs" style="left:401px;top:60px;font-size:38px">What does it cost?</h2>
  <p class="body-copy abs" style="left:401px;top:108px;width:700px">Lorem ipsum dolor sit amet, consectetur adipisicing elit, sed do eiusmod tempor incididunt ut labore et dolore magna aliqua. Ut enim ad minim veniam, quis nostrud exercitation ullamco laboris nisi ut aliquip ex ea commodo consequat. Duis aute irure dolor in reprehenderit in voluptate velit esse cillum dolore eu fugiat nulla pariatur.</p>
  <a class="btn-dark abs" style="left:401px;top:226px;width:108px;height:35px">Learn More</a>
</section>

<section class="row row-white abs" style="top:1037px;height:291px">
  <h2 class="heading abs" style="left:112px;top:48px;font-size:38px">About the same as 1</h2>
  <p class="body-copy abs" style="left:112px;top:96px;width:700px">Lorem ipsum dolor sit amet, consectetur adipisicing elit, sed do eiusmod tempor incididunt ut labore et dolore magna aliqua. Ut enim ad minim veniam, quis nostrud exercitation ullamco laboris nisi ut aliquip ex ea commodo consequat. Duis aute irure dolor in reprehenderit in voluptate velit esse cillum dolore eu fugiat nulla pariatur.</p>
  <a class="btn-dark abs" style="left:112px;top:211px;width:107px;height:35px">Learn More</a>
  <div class="abs art" style="left:824px;top:4px;width:274px;height:287px;background:radial-gradient(circle at 45% 55%,#2a1a14 0,#5a3a2a 25%,#e8e3dc 45%,#ffffff 70%)" role="img" aria-label="Photo of a glass cup of coffee topped with whipped cream"></div>
</section>

<section class="row row-grey abs" style="top:1328px;height:307px">
  <div class="abs art" style="left:146px;top:25px;width:196px;height:177px;background:radial-gradient(circle at 45% 55%,#e9a52a 0,#d88a18 35%,#f4efe4 60%,#f2f2f2 75%)" role="img" aria-label="Photo of a foaming mug of beer"></div>
  <h2 class="heading abs" style="left:401px;top:50px;font-size:38px;line-height:48px">A day &amp; guranteed less than a really<br>good night out eith the gang</h2>
  <p class="body-copy abs" style="left:401px;top:147px;width:700px">Lorem ipsum dolor sit amet, consectetur adipisicing elit, sed do eiusmod tempor incididunt ut labore et dolore magna aliqua.</p>
  <a class="btn-dark abs" style="left:401px;top:214px;width:108px;height:36px">Learn More</a>
</section>

<section class="price-band abs">
  <div class="price-band-text abs">See complete pricing details here</div>
  <a class="price-band-btn abs">Request an Order Now</a>
</section>

<section class="row row-white abs" style="top:1753px;height:257px">
  <div class="abs art" style="left:205px;top:55px;width:235px;height:110px;background:radial-gradient(ellipse,rgba(222,205,180,.45),rgba(255,255,255,0) 70%)" role="img" aria-label="Faint rocket illustration in the background"></div>
  <h2 class="heading abs" style="left:112px;top:42px;font-size:38px">If you are unhapp?</h2>
  <p class="body-copy abs" style="left:112px;top:90px;width:580px">Lorem ipsum dolor sit amet, consectetur adipisicing elit, sed do eiusmod tempor incididunt ut labore et dolore magna aliqua.</p>
  <div class="partner abs" style="left:112px;top:160px">
    <div class="partner-mark"></div>
    <div class="partner-name">Quillhaven</div>
  </div>
  <div class="abs art" style="left:844px;top:27px;width:244px;height:230px;background:linear-gradient(#f4f4f4 0,#e8e8e8 55%,#2a2f3a 80%,#1c2029 100%)" role="img" aria-label="Photo of a person holding a round sad-face sign in front of them"></div>
</section>

<section class="calc abs">
  <h2 class="calc-title abs">Test Your Website Now!<br>How Many More Customers Could You Get Every Month</h2>
  <div class="field abs" style="left:134px;width:191px">Visitors per month</div>
  <div class="field abs" style="left:334px;width:199px">Current conversion rate in %</div>
  <div class="field abs" style="left:541px;width:224px">Improve conversion rate, 13%</div>
  <div class="field abs" style="left:773px;width:203px">Average purchase in SEK</div>
  <div class="field abs" style="left:984px;width:84px;padding-left:20px">EUR <svg style="margin-left:16px" width="10" height="6" viewBox="0 0 10 6"><path d="M0 0h10L5 6z" fill="#333"/></svg></div>
  <a class="calc-btn abs">Calculate Now</a>
</section>

<section class="abs" style="left:0;top:2394px;width:1200px;height:413px">
  <h2 class="heading details-title abs" style="top:58px">See pricing details for most convenient web ever</h2>
  <div class="brand abs" style="left:500px;top:153px;width:200px">
    <div class="brand-mark"></div>
    <div class="brand-name">Sitepelican</div>
    <div class="brand-tag">Most Convenient Web Ever</div>
  </div>
</section>
<a class="demo-btn abs">REQUEST A DEMO</a>

<footer class="site-footer abs">
  <h3 class="foot-head abs" style="left:118px;top:34px">CONTACT US</h3>
  <div class="abs" style="left:118px;top:64px;display:grid;grid-template-columns:58px 1fr">
    <span class="foot-line">Phone</span><span class="foot-line">: +11 (02) 48 317 2250</span>
    <span class="foot-line">Email</span><span class="foot-line">: xyz@sitepelican.com</span>
    <span class="foot-line">Address</span><span class="foot-line" style="line-height:17px;padding-top:3px">: Unit 48, Harbor Lane<br>&nbsp;&nbsp;51207 Cedar Ave<br>&nbsp;&nbsp;Millbrook, OR</span>
  </div>
  <div class="foot-divider abs" style="left:433px"></div>
  <h3 class="foot-head abs" style="left:472px;top:34px">GET IN TOUCH</h3>
  <div class="social abs" style="left:474px"></div>
  <div class="social abs" style="left:515px"></div>
  <div class="social abs" style="left:560px"></div>
  <div class="social abs" style="left:600px;display:flex;align-items:center;justify-content:center"><svg width="16" height="11" viewBox="0 0 16 11"><rect x=".5" y=".5" width="15" height="10" fill="#fff"/><path d="M.5 .5 8 6l7.5-5.5" fill="none" stroke="#0d2436"/></svg></div>
  <div class="foot-line abs" style="left:474px;top:126px;font-weight:600">Subscribe monthly Newsletter</div>
  <div class="sub-input abs">Enter your email address</div>
  <div class="sub-go abs">GO</div>
  <div class="foot-divider abs" style="left:732px"></div>
  <div class="brand abs" style="left:805px;top:20px;width:200px">
    <div class="brand-mark" style="background:#e8e8e8"></div>
    <div class="brand-name" style="color:#fff">Sitepelican</div>
    <div class="brand-tag" style="color:#fff">Most Convenient Web Ever</div>
  </div>
  <div class="foot-line abs" style="left:806px;top:132px">Copyright © 2014 . All rights Reserved</div>
  <div class="contact-tab abs">Contact us! <svg width="12" height="8" viewBox="0 0 12 8"><path d="M1 7 6 2l5 5" fill="none" stroke="#fff" stroke-width="2"/></svg></div>
</footer>

</body>
</html>
```